Plum & Us Business Card Design

Plum & Us is a company that makes treats and real food for people with food allergies, illnesses and those that like to eat clean. We like to take good old fashioned favorites and create a clean, healthy version of it without losing any of the addictive ‘yumminess’ of it.All of our products are made with Organic ingredients and we aim to be as sustainable as possible therefore I would like this to be reflected in our business cards. I like the thought of using chia seeds in the business card maybe so that people could grow their own.

Industry/Entity Type

Health And Wellness

Contact Information for Business Card

Plum & Uswww.plumandus.com.aumarnie@plumandus.com.auP: 0431 596 218 Facebook and Instagram logos

Requirements
Must have
• Logo - does not have to be the exact logo as long as it is close and fits in with the other information I have asked for (sustainable & Organic, recycled etc.)
• See the photo with the treats for a picture of the logo

```html
<!DOCTYPE html>
<html lang="en">
<head>
<meta charset="utf-8">
<title>Plum &amp; Us Business Card</title>
<link rel="stylesheet" href="https://fonts.googleapis.com/css2?family=Open+Sans:wght@400;700&display=swap">
<style>
  :root {
    --backdrop: #e9e7e3;
    --card: #fbfbfa;
    --plum: #3d3a7c;
    --leaf: #6f9a3e;
    --ink-soft: #4a4780;
    --rule: #3d3a7c;
  }
  * { box-sizing: border-box; margin: 0; padding: 0; }
  html, body {
    width: 1200px;
    height: 1022px;
    overflow: hidden;
    background: var(--backdrop);
    font-family: "Open Sans", Arial, sans-serif;
  }
  .stage {
    width: 1200px;
    height: 1022px;
    display: flex;
    align-items: center;
    justify-content: center;
  }
  .business-card {
    position: relative;
    width: 1000px;
    height: 572px;
    background: var(--card);
    border-radius: 22px;
    box-shadow: 0 6px 24px rgba(0,0,0,0.12);
    display: flex;
    align-items: center;
    padding: 0 90px 40px 110px;
  }
  .brand-name {
    font-size: 76px;
    font-weight: 400;
    color: var(--plum);
    letter-spacing: 1px;
    white-space: nowrap;
  }
  .divider {
    width: 2px;
    height: 150px;
    background: var(--rule);
    margin: 0 34px 0 40px;
    flex: none;
  }
  .contact-block { color: var(--ink-soft); }
  .person-name {
    font-size: 36px;
    font-weight: 700;
    color: var(--plum);
    letter-spacing: 0.5px;
    line-height: 1.1;
    white-space: nowrap;
  }
  .person-role {
    font-size: 20px;
    color: var(--leaf);
    letter-spacing: 1px;
    margin-bottom: 14px;
  }
  .contact-list { list-style: none; }
  .contact-list li {
    display: flex;
    align-items: center;
    font-size: 22px;
    line-height: 1.45;
    color: var(--ink-soft);
    white-space: nowrap;
  }
  .contact-list svg {
    width: 16px;
    height: 16px;
    margin-right: 12px;
    flex: none;
  }
  .social-links {
    position: absolute;
    top: 40px;
    right: 44px;
    display: flex;
    gap: 12px;
  }
  .social-links span {
    width: 20px;
    height: 20px;
    border-radius: 4px;
    background: var(--plum);
  }
</style>
</head>
<body>
<main class="stage">
  <section class="business-card">
    <div class="social-links" aria-label="Social media profiles">
      <span role="img" aria-label="Social profile one"></span>
      <span role="img" aria-label="Social profile two"></span>
    </div>

    <h1 class="brand-name">Plum &amp; Us</h1>

    <div class="divider"></div>

    <div class="contact-block">
      <p class="person-name">TESSA MARLOW</p>
      <p class="person-role">DIRECTOR</p>
      <ul class="contact-list">
        <li>
          <svg viewBox="0 0 16 16" aria-hidden="true"><path fill="#6f9a3e" d="M4 1.5l2.2 2.6-1.3 1.6c.9 2 2.5 3.6 4.5 4.5l1.6-1.3 2.6 2.2-1.4 2.4C7.3 13.2 2.8 8.7 1.6 3z"/></svg>
          0431 596 218
        </li>
        <li>
          <svg viewBox="0 0 16 16" aria-hidden="true"><rect x="1.5" y="3.5" width="13" height="9" fill="none" stroke="#6f9a3e" stroke-width="1.6"/><path d="M1.5 3.5l6.5 5 6.5-5" fill="none" stroke="#6f9a3e" stroke-width="1.6"/></svg>
          marnie@plumandus.com.au
        </li>
        <li>
          <svg viewBox="0 0 16 16" aria-hidden="true"><circle cx="8" cy="8" r="6.5" fill="none" stroke="#6f9a3e" stroke-width="1.4"/><ellipse cx="8" cy="8" rx="2.8" ry="6.5" fill="none" stroke="#6f9a3e" stroke-width="1.2"/><path d="M1.5 8h13" stroke="#6f9a3e" stroke-width="1.2"/></svg>
          www.plumandus.com.au
        </li>
      </ul>
    </div>
  </section>
</main>
</body>
</html>
```